PPE EQIUPMENT

WE WOULD LIKE TO PRODUCE 2 DIFFERENT BANNERS TO BE PLACED OUTSIDE OF OUR WAREHOUSE TO ADVERTISE THAT WE HAVE FACE MASKS, HAND SANITISERS, DISINFECTANT SPRAY, FACE SHIELDS AND HAND SOAP. THE SIZE OF EACH BANNER WILL BE , portrait to be (W) 140 cm x (H) 250 cm, with 4 x eyelets. THE BANNER IS TO STATE PPE EQUIPMENT AVAILABLE HERE AND SHOW OUR PHONE NUMBER 0207-946-0318. FINALLY WE WILL REQUIRE SOME IMAGES OF THE PRODUCTS IF YOU CAN SUPPLY THESE. THANKS

```html
<!DOCTYPE html>
<html lang="en">
<head>
<meta charset="utf-8">
<title>PPE Equipment Available – Banner</title>
<link rel="stylesheet" href="https://fonts.googleapis.com/css2?family=Barlow:wght@500&family=Roboto:wght@700;900&display=swap">
<style>
  :root {
    --navy: #213a72;
    --band-blue: #1a6db5;
    --accent-blue: #1770b9;
    --ink: #333333;
    --list-ink: #3a3a3a;
    --white: #ffffff;
    --pale-blue: #bed2f7;
    --eyelet-ring: #8a8a8a;
    --soap: #eeebe2;
    --mask: #9fd8ea;
    --sanitiser: #2f86e6;
    --spray: #1ab8f4;
    --shield: #c9d6ee;
  }
  html, body {
    margin: 0;
    padding: 0;
    width: 672px;
    height: 1200px;
    overflow: hidden;
  }
  .banner {
    position: relative;
    width: 672px;
    height: 1200px;
    overflow: hidden;
    background: linear-gradient(180deg, var(--white) 0%, var(--white) 45%, #eef2fd 62%, #d6e2fa 82%, var(--pale-blue) 100%);
    font-family: "Roboto", Arial, sans-serif;
  }
  .header-backdrop {
    position: absolute;
    top: 0;
    left: 0;
    width: 672px;
    height: 500px;
  }
  .brand-name {
    position: absolute;
    top: 50px;
    left: 0;
    width: 672px;
    text-align: center;
    margin: 0;
    font-family: "Barlow", Arial, sans-serif;
    font-weight: 500;
    font-size: 40px;
    letter-spacing: 1px;
    color: var(--white);
    line-height: 1;
  }
  .product-lineup {
    position: absolute;
    left: 20px;
    top: 140px;
    width: 632px;
    height: 360px;
    background:
      radial-gradient(62px 72px at 62px 277px, var(--soap) 0%, var(--soap) 55%, rgba(238,235,226,0) 100%),
      radial-gradient(58px 105px at 167px 220px, var(--mask) 0%, var(--mask) 55%, rgba(159,216,234,0) 100%),
      radial-gradient(42px 98px at 278px 210px, var(--sanitiser) 0%, var(--sanitiser) 55%, rgba(47,134,230,0) 100%),
      radial-gradient(66px 152px at 396px 160px, var(--spray) 0%, var(--spray) 55%, rgba(26,184,244,0) 100%),
      radial-gradient(88px 72px at 536px 243px, var(--shield) 0%, var(--shield) 55%, rgba(201,214,238,0) 100%);
  }
  .headline {
    position: absolute;
    top: 497px;
    left: 0;
    width: 672px;
    margin: 0;
    text-align: center;
    font-weight: 900;
    font-size: 68px;
    line-height: 79px;
    color: var(--ink);
    letter-spacing: -0.5px;
  }
  .product-list {
    position: absolute;
    top: 693px;
    left: 0;
    width: 672px;
    margin: 0;
    padding: 0;
    list-style: none;
  }
  .product-list li {
    display: flex;
    justify-content: center;
    align-items: center;
    gap: 22px;
    height: 47px;
    font-weight: 700;
    font-size: 30px;
    color: var(--list-ink);
    padding-left: 10px;
  }
  .tick {
    width: 24px;
    height: 24px;
    flex: none;
  }
  .call-label {
    position: absolute;
    top: 957px;
    left: 0;
    width: 672px;
    margin: 0;
    text-align: center;
    font-weight: 700;
    font-size: 54px;
    line-height: 64px;
    color: var(--ink);
  }
  .phone {
    position: absolute;
    top: 1024px;
    left: 0;
    width: 684px;
    margin: 0;
    text-align: center;
    font-weight: 900;
    font-size: 67px;
    line-height: 76px;
    color: var(--accent-blue);
  }
  .eyelet {
    position: absolute;
    width: 42px;
    height: 42px;
  }
  .eyelet.top-left { left: 41px; top: 25px; }
  .eyelet.top-right { left: 589px; top: 25px; }
  .eyelet.bottom-left { left: 41px; top: 1133px; }
  .eyelet.bottom-right { left: 589px; top: 1133px; }
</style>
</head>
<body>
<div class="banner">
  <svg class="header-backdrop" viewBox="0 0 672 500" aria-hidden="true">
    <defs>
      <linearGradient id="navyFade" x1="0" y1="0" x2="1" y2="1">
        <stop offset="0" stop-color="#223c76"/>
        <stop offset="0.5" stop-color="#233d77"/>
        <stop offset="1" stop-color="#1d3570"/>
      </linearGradient>
    </defs>
    <path d="M0 0 H672 V420 L0 420 Z" fill="url(#navyFade)"/>
    <path d="M0 372 Q336 240 672 372 L672 412 Q336 270 0 412 Z" fill="var(--band-blue)"/>
    <path d="M0 412 Q336 270 672 412 L672 500 L0 500 Z" fill="#ffffff"/>
  </svg>

  <h1 class="brand-name">NORTHGATE FURNITURE</h1>

  <div class="product-lineup" role="img" aria-label="Product photos: bar of soap, surgical face mask, hand sanitiser pump bottle, blue disinfectant spray bottle and clear face shield"></div>

  <h2 class="headline">PPE EQUIPMENT<br>AVAILABLE</h2>

  <ul class="product-list">
    <li><svg class="tick" viewBox="0 0 24 24" aria-hidden="true"><circle cx="12" cy="12" r="12" fill="var(--accent-blue)"/><path d="M6.5 12.3 L10.3 16 L17.5 8.6" fill="none" stroke="#fff" stroke-width="2.8" stroke-linecap="round" stroke-linejoin="round"/></svg>FACE MASKS</li>
    <li><svg class="tick" viewBox="0 0 24 24" aria-hidden="true"><circle cx="12" cy="12" r="12" fill="var(--accent-blue)"/><path d="M6.5 12.3 L10.3 16 L17.5 8.6" fill="none" stroke="#fff" stroke-width="2.8" stroke-linecap="round" stroke-linejoin="round"/></svg>HAND SANITISERS</li>
    <li><svg class="tick" viewBox="0 0 24 24" aria-hidden="true"><circle cx="12" cy="12" r="12" fill="var(--accent-blue)"/><path d="M6.5 12.3 L10.3 16 L17.5 8.6" fill="none" stroke="#fff" stroke-width="2.8" stroke-linecap="round" stroke-linejoin="round"/></svg>DISINFECTANT SPRAY</li>
    <li><svg class="tick" viewBox="0 0 24 24" aria-hidden="true"><circle cx="12" cy="12" r="12" fill="var(--accent-blue)"/><path d="M6.5 12.3 L10.3 16 L17.5 8.6" fill="none" stroke="#fff" stroke-width="2.8" stroke-linecap="round" stroke-linejoin="round"/></svg>FACE SHIELDS</li>
    <li><svg class="tick" viewBox="0 0 24 24" aria-hidden="true"><circle cx="12" cy="12" r="12" fill="var(--accent-blue)"/><path d="M6.5 12.3 L10.3 16 L17.5 8.6" fill="none" stroke="#fff" stroke-width="2.8" stroke-linecap="round" stroke-linejoin="round"/></svg>HAND SOAP.</li>
  </ul>

  <p class="call-label">Call us on</p>
  <p class="phone">0207-946-0318</p>

  <svg class="eyelet top-left" viewBox="0 0 42 42" aria-hidden="true"><circle cx="21" cy="21" r="20" fill="var(--eyelet-ring)"/><circle cx="21" cy="21" r="16.5" fill="#fff"/></svg>
  <svg class="eyelet top-right" viewBox="0 0 42 42" aria-hidden="true"><circle cx="21" cy="21" r="20" fill="var(--eyelet-ring)"/><circle cx="21" cy="21" r="16.5" fill="#fff"/></svg>
  <svg class="eyelet bottom-left" viewBox="0 0 42 42" aria-hidden="true"><circle cx="21" cy="21" r="20" fill="var(--eyelet-ring)"/><circle cx="21" cy="21" r="16.5" fill="#fff"/></svg>
  <svg class="eyelet bottom-right" viewBox="0 0 42 42" aria-hidden="true"><circle cx="21" cy="21" r="20" fill="var(--eyelet-ring)"/><circle cx="21" cy="21" r="16.5" fill="#fff"/></svg>
</div>
</body>
</html>
```